BRIGHTWATER LENDING PARTNERS PTY LTD

hi guys,
i need to create a facebook page for my company brightwater lending partners.
the website for the company is www.brightwaterlp.com.au for you to reference from.
i want something very professional and cool at the same tipe.

Industry/Entity Type

Finance

Requirements
Must have
• Features from my website
• www.brightwaterlendingpartners.com.au
Nice to have

```html
<!DOCTYPE html>
<html lang="en">
<head>
<meta charset="utf-8">
<title>Brightwater Lending Partners – Cover</title>
<link rel="stylesheet" href="https://fonts.googleapis.com/css2?family=Open+Sans:wght@400;600;700&display=swap">
<style>
  :root {
    --sky-top: #8fa3b4;
    --sky-mid: #5f7384;
    --road-dark: #2e3a45;
    --slate: #3b4a57;
    --panel: #34434f;
    --orange-soft: rgba(242, 106, 27, 0.55);
    --white: #ffffff;
    --text-shadow: rgba(0, 0, 0, 0.55);
  }
  html, body {
    margin: 0;
    padding: 0;
    overflow: hidden;
    background: #ffffff;
  }
  .cover {
    position: relative;
    width: 1200px;
    height: 444px;
    overflow: hidden;
    font-family: "Open Sans", Arial, sans-serif;
    color: var(--white);
  }
  .cover__photo {
    position: absolute;
    inset: 0;
    background:
      radial-gradient(ellipse 420px 200px at 830px 250px, rgba(140,170,200,0.55), transparent 70%),
      linear-gradient(180deg, var(--sky-top) 0%, var(--sky-mid) 38%, #4c5c68 60%, var(--road-dark) 100%);
  }
  .cover__accent {
    position: absolute;
    inset: 0;
    background: linear-gradient(160deg, transparent 45%, var(--orange-soft) 62%, var(--slate) 80%, var(--road-dark) 100%);
  }
  .features {
    position: absolute;
    inset: 0;
    margin: 0;
    padding: 0;
    list-style: none;
    font-weight: 600;
    font-size: 26.5px;
    line-height: 1;
    text-shadow: 0 1px 3px var(--text-shadow);
  }
  .features li {
    position: absolute;
    white-space: nowrap;
  }
  .features li::before {
    content: "•";
    margin-right: 6px;
  }
  .features--left li { left: 26px; }
  .features--right li { left: 734px; }
  .features li.row-1 { top: 33px; }
  .features li.row-2 { top: 84px; }
  .features li.row-3 { top: 137px; }
  .brand-panel {
    position: absolute;
    left: 38px;
    top: 212px;
    width: 240px;
    height: 250px;
    background: linear-gradient(180deg, #3f4f5c 0%, var(--panel) 100%);
    border: 4px solid var(--white);
    box-sizing: border-box;
    box-shadow: 0 2px 8px rgba(0,0,0,0.4);
    display: flex;
    align-items: center;
    justify-content: center;
    padding: 0 16px 20px;
  }
  .brand-name {
    margin: 0;
    font-weight: 600;
    font-size: 19px;
    line-height: 1.3;
    text-align: center;
    color: var(--white);
    letter-spacing: 0.5px;
  }
  .tagline {
    position: absolute;
    right: 30px;
    top: 356px;
    margin: 0;
    text-align: right;
    font-weight: 400;
    font-size: 31px;
    line-height: 37px;
    white-space: nowrap;
  }
  .tagline strong { font-weight: 700; }
</style>
</head>
<body>
  <div class="cover">
    <div class="cover__photo" role="img" aria-label="Silver-blue sports car driving along a winding mountain road under an overcast sky"></div>
    <div class="cover__accent" role="img" aria-label="Decorative orange and slate sweeping accent across the lower right"></div>

    <ul class="features features--left">
      <li class="row-1">Quick &amp; Easy, Same Day Approvals</li>
      <li class="row-2">Access Australia’s Most Trusted Lenders</li>
      <li class="row-3">Professional Advice: New, Used, Private or Dealer sale</li>
    </ul>
    <ul class="features features--right">
      <li class="row-1">Low Rates</li>
      <li class="row-2">100% Finance Available</li>
    </ul>

    <div class="brand-panel">
      <p class="brand-name">BRIGHTWATER LENDING PARTNERS PTY LTD</p>
    </div>

    <p class="tagline">It’s <strong>Time</strong> to<br>finance <strong>YOUR</strong> Dream</p>
  </div>
</body>
</html>
```